Visitenkarten-Design für Immobilienunternehmen
Zielgruppe
Wir sind ein Immobilienunternehmen mit 2 Büros - alle Zielgruppen, jung und alt, arm und reich, Käufer und Verkäufer, privat und gewerblich suchen ein neues hochwertiges Design für die Visitenkarte
Aufgabenstellung
seriös, nicht angestaubt, Firmenfarben (rot,blau, weiß, siehe Bilder)
2-seitg bedruckt (allgemein auf der einen Seite, personenvorstellung mit bild auf der anderen seite)
Ein Visitenkartendesign für 2 Personen

```html
<!DOCTYPE html>
<html lang="de">
<head>
<meta charset="utf-8">
<title>Visitenkarte Miriam Adler</title>
<link rel="stylesheet" href="https://fonts.googleapis.com/css2?family=Montserrat:wght@400;600;700;800&display=swap">
<style>
  :root {
    --brand-blue: #1b2f8c;
    --brand-blue-light: #2a4bb3;
    --brand-red: #e3140d;
    --frame-mid: #7a2158;
    --paper: #ffffff;
    --photo-green: #8fa56a;
    --photo-warm: #b99a80;
  }
  * { margin: 0; padding: 0; box-sizing: border-box; }
  html, body { width: 1200px; height: 777px; overflow: hidden; background: var(--paper); }
  body { font-family: "Montserrat", Arial, sans-serif; }

  .card {
    position: relative;
    width: 1200px;
    height: 777px;
    background: linear-gradient(90deg, var(--brand-blue) 0%, var(--frame-mid) 65%, var(--brand-red) 100%);
    padding: 17px;
  }
  .card-inner {
    position: relative;
    width: 100%;
    height: 100%;
    background: var(--paper);
  }

  .portrait {
    position: absolute;
    left: 47px;
    top: 75px;
    width: 382px;
    height: 382px;
    border-radius: 50%;
    border: 7px solid var(--brand-blue);
    background:
      radial-gradient(circle at 55% 40%, var(--photo-warm) 0%, var(--photo-warm) 22%, transparent 45%),
      radial-gradient(circle at 50% 95%, var(--brand-blue-light) 0%, var(--brand-blue) 40%, transparent 60%),
      linear-gradient(135deg, #c9b8a6 0%, var(--photo-green) 70%, #5f7a3e 100%);
  }

  .identity {
    position: absolute;
    left: 521px;
    top: 92px;
    color: var(--brand-blue);
  }
  .identity-name {
    font-weight: 800;
    font-size: 50px;
    line-height: 60px;
    letter-spacing: 0.2px;
  }
  .identity-role {
    font-weight: 400;
    font-size: 35px;
    line-height: 45px;
  }

  .contact {
    position: absolute;
    left: 521px;
    top: 303px;
    list-style: none;
    color: var(--brand-red);
    font-weight: 700;
    font-size: 30px;
    line-height: 55px;
  }

  .referral {
    position: absolute;
    left: 55px;
    top: 565px;
    color: var(--brand-blue);
    font-weight: 400;
    font-size: 31px;
    line-height: 43px;
  }

  .partner-badge {
    position: absolute;
    left: 859px;
    top: 581px;
    width: 102px;
    height: 102px;
    background: var(--brand-blue);
  }

  .brand-mark {
    position: absolute;
    left: 1010px;
    top: 610px;
    display: flex;
    align-items: center;
    gap: 10px;
    color: var(--brand-red);
    font-weight: 800;
    font-size: 32px;
  }
  .brand-mark-dot {
    width: 22px;
    height: 22px;
    background: var(--brand-red);
  }
</style>
</head>
<body>
  <div class="card">
    <div class="card-inner">
      <div class="portrait" role="img" aria-label="Porträtfoto der Immobilienberaterin im blauen Blazer"></div>

      <div class="identity">
        <div class="identity-name">Miriam Adler</div>
        <div class="identity-role">Büromanagement</div>
        <div class="identity-role">Immobilienberaterin</div>
      </div>

      <ul class="contact">
        <li>0160/4827391</li>
        <li>info@hans-berger-immobilien.de</li>
        <li>hans-berger-immobilien.de</li>
      </ul>

      <p class="referral">
        Kennen Sie jemanden, der ein Haus oder<br>
        eine Wohnung kaufen oder verkaufen möch-<br>
        te? Bitte rufen Sie mich an. Ich freue mich!
      </p>

      <div class="partner-badge" aria-hidden="true"></div>

      <div class="brand-mark">
        <span class="brand-mark-dot"></span>
        <span>NOVA</span>
      </div>
    </div>
  </div>
</body>
</html>
```